Sun Petal Custom Spray Tanning Studio

I have attached most of the information that I would like in my brochure. However, I would like the brochure to be more elegant and professional. I am no longer offering mobile tanning, however, I will be located at: 418 W Larkin Street, Myrtle Beach, SC 29577. 843-271-5046 and I am by appointment only.

Reason: I found designs that I like, however: Spelling and grammar is critical. Please make sure that every word is spelled correctly. I am also changing my colors with my new business cards.

Target Market(s)

My clients have an average to above average income. They are health conscience and take good care of themselves. Into high end quality work and willing to pay for it.

Industry/Entity Type

It Professional

Font styles to use
Serif
Decorative
Script

Requirements
Must have
• Correct Spelling and grammar are a must. Please make sure everything is spelled correctly, punctuated properly and words are used exactly like I have it my brochure.
Nice to have
• Elegant and Classy
Should not have
• Nothing to do with Mobile Tanning.
On the front, I prefer the wording.... Call and Make your appointments at (843)271-5046. Visit us online at www.sunpetalbronze.com or email me at maribel@sunpetalbronze.com

```html
<!DOCTYPE html>
<html lang="en">
<head>
<meta charset="utf-8">
<title>Sun Petal – Custom Sunless Tanning Brochure</title>
<link href="https://fonts.googleapis.com/css2?family=Advent+Pro:wght@300;400;500&family=Kaushan+Script&family=Great+Vibes&display=swap" rel="stylesheet">
<style>
  :root{
    --stage:#9d9596;
    --brown-deep:#1e0c08;
    --brown:#2c150e;
    --brown-mid:#4a2a1c;
    --gold:#c9aa78;
    --gold-light:#e6cf9f;
    --gold-dark:#7a5c36;
    --rose:#c89a8c;
    --coral:#f29a73;
    --cream:#f1e3cc;
    --text-soft:#d9c7b3;
  }
  *{box-sizing:border-box;margin:0;padding:0}
  html,body{width:1200px;height:1083px;overflow:hidden}
  body{background:var(--stage);font-family:"Advent Pro",sans-serif;position:relative}
  .brochure{position:absolute;left:30px;top:92px;width:1140px;height:900px;display:flex;box-shadow:0 20px 40px rgba(0,0,0,.25)}
  .panel{position:relative;width:380px;height:900px;overflow:hidden}

  /* Services panel */
  .services{background:linear-gradient(180deg,var(--brown) 0%,var(--brown-deep) 100%)}
  .services__title{position:absolute;left:48px;top:58px;font-size:42px;color:var(--cream);font-weight:300;letter-spacing:1px;line-height:1.1}
  .script{font-family:"Kaushan Script",cursive;color:var(--coral);font-weight:400}
  .service-list{position:absolute;left:26px;top:136px;width:330px;list-style:none}
  .service{position:relative;height:38px;display:flex;align-items:center}
  .service--band::before{content:"";position:absolute;inset:2px 0;background:linear-gradient(90deg,rgba(200,154,140,.15),var(--rose) 55%,rgba(200,154,140,.85))}
  .service__num{position:relative;width:34px;font-size:24px;color:var(--cream);font-weight:300}
  .service__name{position:relative;flex:1;text-align:center;font-size:17px;color:var(--cream);letter-spacing:.5px}
  .service--band .service__name{color:#8c4f4a}
  .service--tall{height:54px}
  .service--tall .service__name{line-height:1.15}
  .services__copy{position:absolute;left:26px;top:388px;width:330px;font-size:12.5px;line-height:1.35;color:var(--text-soft);text-align:justify;letter-spacing:.3px}
  .care-box{position:absolute;left:26px;top:494px;width:330px;height:356px;border:1px solid var(--gold-dark);border-radius:16px;padding:16px 20px}
  .care-box__intro{font-size:12.2px;line-height:1.32;color:var(--text-soft);text-align:justify}
  .care-box__head{margin:14px -20px 6px;padding:1px 20px;font-family:"Great Vibes",cursive;font-size:18px;color:var(--brown);background:linear-gradient(90deg,var(--gold-light),var(--gold) 60%,var(--gold-dark))}
  .care-box ul{list-style:none;font-size:12.2px;line-height:1.32;color:var(--text-soft)}
  .care-box li::before{content:"• "}
  .band-foot{position:absolute;left:0;bottom:0;width:100%;height:32px;background:linear-gradient(90deg,var(--gold-dark),var(--gold-light) 50%,var(--gold-dark))}

  /* Prices panel */
  .prices{background:var(--brown-deep)}
  .prices__title{position:absolute;left:58px;top:40px;font-size:40px;line-height:1.1}
  .price-list{position:absolute;left:36px;top:118px;width:316px;list-style:none}
  .price{height:58px}
  .price__item{height:24px;padding-right:20px;text-align:right;font-size:15px;line-height:24px;letter-spacing:.5px;color:rgba(60,30,20,.7)}
  .price:nth-child(odd) .price__item{background:linear-gradient(90deg,var(--gold-dark),var(--gold) 60%,var(--gold-light))}
  .price:nth-child(even) .price__item{background:linear-gradient(90deg,#7d5a52,var(--rose) 60%,#e2c1b3)}
  .price__amount{padding-right:20px;text-align:right;font-size:20px;color:var(--coral);line-height:30px}
  .contact{position:absolute;left:0;bottom:0;width:100%;height:182px;background:linear-gradient(90deg,#a3855a,var(--gold-light) 50%,#a3855a);text-align:center;color:#5b4630;padding-top:38px}
  .contact__lead{font-size:12px;letter-spacing:1px}
  .contact__phone{font-size:30px;font-weight:300;letter-spacing:2px;line-height:1.1}
  .contact__address{font-size:12.5px;letter-spacing:.6px;padding-bottom:8px;border-bottom:1px solid rgba(91,70,48,.5);margin:0 66px}
  .contact__web{font-size:20px;letter-spacing:.5px;margin-top:4px}

  /* Cover panel */
  .cover{background:var(--brown)}
  .cover__photo{position:absolute;left:0;top:18px;width:380px;height:670px;background:radial-gradient(ellipse at 30% 20%,#e7c577 0%,#c49a4c 40%,#8c6a3c 70%,#5c4328 100%)}
  .cover__offer{position:absolute;left:0;top:56px;width:100%;text-align:center;color:rgba(110,80,45,.9);font-size:15px;line-height:1.35;font-weight:300}
  .cover__offer em{font-style:normal;font-size:19px}
  .band-top{position:absolute;left:0;top:0;width:100%;height:18px;background:linear-gradient(90deg,var(--gold-dark),var(--gold-light) 50%,var(--gold-dark))}
  .band-mid{position:absolute;left:0;top:688px;width:100%;height:16px;background:linear-gradient(90deg,var(--gold-dark),var(--gold-light) 50%,var(--gold-dark))}
  .cover__base{position:absolute;left:0;top:704px;width:100%;height:196px;background:linear-gradient(180deg,var(--brown-mid),var(--brown))}
  .cover__name{position:absolute;left:0;top:34px;width:100%;text-align:center;font-size:62px;font-weight:400;color:var(--cream);line-height:1.2}
  .cover__tagline{position:absolute;left:0;top:122px;width:100%;text-align:center;font-family:"Great Vibes",cursive;font-size:24px;color:var(--cream)}
</style>
</head>
<body>
<main class="brochure">

  <section class="panel services">
    <h2 class="services__title"><span class="script">Services</span> we offer</h2>
    <ol class="service-list">
      <li class="service service--band"><span class="service__num">01</span><span class="service__name">Bronze Tanning Sessions</span></li>
      <li class="service"><span class="service__num">02</span><span class="service__name">Clear Tanning Sessions</span></li>
      <li class="service service--band"><span class="service__num">03</span><span class="service__name">Anti-aging Beauty Elixirs</span></li>
      <li class="service"><span class="service__num">04</span><span class="service__name">PH Balance Normalization Treatments</span></li>
      <li class="service service--band"><span class="service__num">05</span><span class="service__name">Shimmer Application</span></li>
      <li class="service service--tall"><span class="service__num">06</span><span class="service__name">Tanning Packages for all<br>types of parties and events</span></li>
    </ol>
    <p class="services__copy">Each session is applied by a certified tanning technician that will not only give you the most natural looking customized spray tan, but will leave your skin radiant and hydrated. In addition, the tanning session will improve firmness and camouflage spider veins while allowing you to feel more confident on and off the beach.</p>
    <div class="care-box">
      <p class="care-box__intro">For the optimal tanning experience, make sure you follow Sun Petal's recommendations for preparation and aftercare. This will ensure you obtain the best results possible from your sunless tanning experience.</p>
      <h3 class="care-box__head">Preparation</h3>
      <ul>
        <li>Shower, shave and exfoliate at least 1 day before you tan.</li>
        <li>Come in for your appointment with clean dry skin, no lotion, makeup or deodorant.</li>
        <li>Wear dark, loose clothes, nothing hugging your body as this will leave lines.</li>
      </ul>
      <h3 class="care-box__head">Aftercare</h3>
      <ul>
        <li>Wait 8-10 hours before showering.</li>
        <li>Do not swim, use hot tubs or exercise which will cause you to sweat and could remove your sunless tanner.</li>
        <li>Hydrate your skin with a moisturizer twice a day and drink plenty of water.</li>
      </ul>
    </div>
    <div class="band-foot"></div>
  </section>

  <section class="panel prices">
    <h2 class="prices__title script">Prices</h2>
    <ul class="price-list">
      <li class="price"><div class="price__item">Bronze Tanning Session</div><div class="price__amount">$55.00</div></li>
      <li class="price"><div class="price__item">Clear Tanning Session</div><div class="price__amount">$55.00</div></li>
      <li class="price"><div class="price__item">Anti-aging Beauty Elixir</div><div class="price__amount">$55.00</div></li>
      <li class="price"><div class="price__item">PH Balance Treatment</div><div class="price__amount">$55.00</div></li>
      <li class="price"><div class="price__item">Shimmer Application</div><div class="price__amount">$55.00</div></li>
      <li class="price"><div class="price__item">Bridal Tanning Package</div><div class="price__amount">$55.00</div></li>
      <li class="price"><div class="price__item">Prom Tanning Package</div><div class="price__amount">$55.00</div></li>
      <li class="price"><div class="price__item">Party Tanning Package</div><div class="price__amount">$55.00</div></li>
      <li class="price"><div class="price__item">Event Tanning Package</div><div class="price__amount">$55.00</div></li>
      <li class="price"><div class="price__item">Touch-up Session</div><div class="price__amount">$55.00</div></li>
    </ul>
    <div class="contact">
      <p class="contact__lead">Call us today and make your appointment</p>
      <p class="contact__phone">(843) 271-5046</p>
      <p class="contact__address">418 W Larkin Street, Myrtle Beach, SC 29577.</p>
      <p class="contact__web">www.sunpetalbronze.com</p>
    </div>
  </section>

  <section class="panel cover">
    <div class="band-top"></div>
    <div class="cover__photo" role="img" aria-label="Photo of a tanned woman in a black swimsuit on a golden sunlit beach"></div>
    <p class="cover__offer">We offer a customized spray tan<br><em>by appointment only.</em></p>
    <div class="band-mid"></div>
    <div class="cover__base">
      <h1 class="cover__name">Sun Petal</h1>
      <p class="cover__tagline">-Custom Sunless Tanning-</p>
    </div>
  </section>

</main>
</body>
</html>
```